Artist needs a business card for her pencil portraits and streetscapes

My mum is an artist and does fabulous portraits and sketches with pencil and needs a business card.
She likes designs that are a bit weird or unusual. The winning design will NOT be a slick modern corporate looking logo. It should be a little bit rustic and different. Interesting patterns and textures would be great, it doesn't even need to look like a business card! Come up with something unique!

Target Market(s)

Older clientele looking for family portraits

Industry/Entity Type

Artists

Contact Information for Business Card

Basically just need the name and contact details

Font styles to use
Decorative
Script

Requirements
Must have
• Lena Brodsworth
• Artist
• 0427913562
• lenabrodsworth@quillpost.example
Nice to have
• Weird artistic backgrounds, interesting textures, unusual designs for an artistic woman.
Should not have
• Nothing ultra modern and nothing corporate looking.

```html
<!DOCTYPE html>
<html lang="en">
<head>
<meta charset="utf-8">
<title>Lena Brodsworth — Artist Business Card</title>
<link rel="stylesheet" href="https://fonts.googleapis.com/css2?family=Rye&family=Open+Sans:wght@500&display=swap">
<style>
  :root {
    --page-bg: #e8e5e0;
    --card-dark: #1d120d;
    --card-mid: #2e1f16;
    --card-warm: #3a2717;
    --ink-orange: #c8702f;
    --ink-tan: #b47a3a;
    --ink-black: #0f0906;
  }
  html, body {
    margin: 0;
    padding: 0;
    width: 1200px;
    height: 1200px;
    overflow: hidden;
    background: var(--page-bg);
  }
  .canvas {
    display: block;
    width: 1200px;
    height: 1200px;
  }
  .name-first,
  .name-last {
    font-family: "Rye", "Georgia", serif;
    fill: var(--ink-orange);
    stroke: var(--ink-black);
    stroke-linejoin: round;
    paint-order: stroke fill;
  }
  .name-first { font-size: 140px; stroke-width: 14px; }
  .name-last { font-size: 60px; stroke-width: 10px; }
  .role-label {
    font-family: "Rye", "Georgia", serif;
    font-size: 40px;
    fill: var(--ink-black);
  }
  .contact-line {
    font-family: "Open Sans", "Helvetica", sans-serif;
    font-weight: 500;
    font-size: 24px;
    fill: var(--ink-tan);
    letter-spacing: 0.5px;
  }
  .divider-dots {
    stroke: var(--ink-tan);
    stroke-width: 4;
    stroke-dasharray: 5 15;
  }
</style>
</head>
<body>
<svg class="canvas" viewBox="0 0 1200 1200" xmlns="http://www.w3.org/2000/svg">
  <defs>
    <linearGradient id="cardTexture" x1="0" y1="0" x2="1" y2="1">
      <stop offset="0" stop-color="var(--card-mid)"/>
      <stop offset="0.5" stop-color="var(--card-dark)"/>
      <stop offset="1" stop-color="var(--card-warm)"/>
    </linearGradient>
    <clipPath id="cardShape">
      <rect width="960" height="590" rx="46"/>
    </clipPath>
  </defs>

  <g class="business-card" transform="translate(120 305)">
    <rect class="card-texture" width="960" height="590" rx="46" fill="url(#cardTexture)"
          role="img" aria-label="Dark stained wood texture background"/>
    <rect class="contact-panel" x="656" y="0" width="304" height="590" fill="#000" opacity="0.12" clip-path="url(#cardShape)"/>

    <g class="name-block">
      <text class="name-first" x="74" y="250" textLength="400" lengthAdjust="spacingAndGlyphs">LENA</text>
      <text class="name-last" x="150" y="352" textLength="345" lengthAdjust="spacingAndGlyphs">BRODSWORTH</text>
    </g>

    <g class="role-badge">
      <rect x="113" y="386" width="387" height="94" rx="47" fill="var(--ink-orange)" stroke="var(--ink-black)" stroke-width="3"/>
      <text class="role-label" x="306" y="448" text-anchor="middle">ARTIST</text>
    </g>

    <line class="divider-dots" x1="656" y1="70" x2="656" y2="512"/>

    <g class="contact-details">
      <text class="contact-line" transform="translate(730 484) rotate(-90)">Voice&#160;&#160;0427913562</text>
      <text class="contact-line" transform="translate(802 484) rotate(-90)">lenabrodsworth@quillpost.example</text>
    </g>
  </g>
</svg>
</body>
</html>
```